Hot air balloon tour company needs a brochure redesign

Look for a fresh new brochure design. Using company logo and colours.
Modern, simple and professional look required
Font styles to use
Sans Serif
Colors
0054AA
0677BA
7BADD7
CADEEF
E8F1F8

```html
<!DOCTYPE html>
<html lang="en">
<head>
<meta charset="utf-8">
<title>Skyward Ballooning – Tri-fold Brochure</title>
<link rel="stylesheet" href="https://fonts.googleapis.com/css2?family=Poppins:wght@400;500;600;700;800;900&family=Sacramento&display=swap">
<style>
  :root{
    --blue-deep:#0054AA;
    --blue:#0677BA;
    --blue-bright:#1ea0dc;
    --blue-soft:#7BADD7;
    --blue-pale:#CADEEF;
    --blue-mist:#E8F1F8;
    --ink:#1d1e22;
    --ink-soft:#2a2d34;
    --white:#ffffff;
    --stage:#e4e5e7;
  }
  *{box-sizing:border-box;margin:0;padding:0}
  html,body{width:1200px;height:3899px;overflow:hidden}
  body{background:var(--stage);font-family:"Poppins",sans-serif;position:relative}
  .spread{position:absolute;left:100px;width:577px;height:448px;transform:scale(1.7331);transform-origin:0 0;background:var(--white);overflow:hidden;box-shadow:0 2px 6px rgba(0,0,0,.12)}
  .spread--outside{top:760px}
  .spread--inside{top:2300px}
  .spread svg.shapes{position:absolute;inset:0;width:577px;height:448px}
  .abs{position:absolute}
  .script{font-family:"Sacramento",cursive;font-weight:400}
  .hotline{line-height:1}
  .hotline__label{font-weight:700;font-size:10.5px;color:var(--ink)}
  .hotline__num{font-weight:800;font-size:27px;color:var(--blue-bright);letter-spacing:.5px;margin-top:1px;position:relative}
  .hotline__num::before{content:"";position:absolute;left:-40px;right:-30px;top:50%;height:1px;background:var(--blue-bright);z-index:-1}
  .hotline__words{font-weight:900;font-size:28px;color:var(--ink);letter-spacing:-.3px}
  .brand{font-weight:700;color:var(--blue-bright);font-size:17px;line-height:1;display:flex;align-items:center;gap:5px}
  .brand__dot{width:9px;height:9px;border-radius:50%;background:var(--blue-bright)}
  .brand__sub{font-weight:500;font-size:7px;color:var(--ink);letter-spacing:1px;margin-top:3px;text-align:center}
  .offer{color:var(--white)}
  .offer__title{font-weight:800;font-size:22px;line-height:1}
  .offer__title .script{font-size:24px;margin-left:2px}
  .offer__list{list-style:none;margin-top:8px}
  .offer__list li{font-weight:600;font-size:6.4px;margin-bottom:7.5px;display:flex;gap:3px;line-height:1.1;text-transform:uppercase}
  .tick{width:6px;height:6px;flex:none;margin-top:.5px}
  .contact{color:var(--white);text-align:center;width:120px}
  .contact__title{font-weight:700;font-size:9px}
  .contact__title .script{font-size:10px}
  .contact__line{font-size:5px;font-weight:500;margin-top:1px}
  .contact svg{width:6px;height:6px;display:block;margin:4px auto 0}
  .web{font-size:5.3px;font-weight:600;color:var(--white);display:flex;align-items:center;gap:3px}
  .web i{width:5px;height:5px;border:1px solid var(--white);border-radius:50%;display:inline-block}
  .tagline{color:var(--white);text-align:center;line-height:.92}
  .tagline .script{font-size:15px;display:block;line-height:.8}
  .tagline strong{font-weight:800;font-size:15px;display:block}
  .feature{text-align:center;color:var(--white)}
  .feature h3{font-weight:700;font-size:13px;color:var(--blue-bright);line-height:1}
  .feature .script{font-size:15px;display:block;line-height:.8;color:var(--white)}
  .feature p{font-size:4.6px;line-height:1.3;margin-top:3px}
  .info h3{font-weight:700;font-size:12px;color:var(--blue-bright);line-height:1}
  .info h3 .script{font-size:14px;color:var(--ink);font-weight:400}
  .info p{font-size:4.6px;line-height:1.3;color:#444;margin-top:4px}
</style>
</head>
<body>

<!-- Outside of the brochure -->
<section class="spread spread--outside">
  <svg class="shapes" viewBox="0 0 577 448">
    <defs>
      <linearGradient id="sunrise" x1="0" y1="0" x2="0" y2="1">
        <stop offset="0" stop-color="#2d3e58"/>
        <stop offset=".35" stop-color="#7b6f70"/>
        <stop offset=".5" stop-color="#e7a040"/>
        <stop offset=".62" stop-color="#5b5a5c"/>
        <stop offset="1" stop-color="#14161b"/>
      </linearGradient>
      <linearGradient id="shade" x1="0" y1="0" x2="0" y2="1">
        <stop offset=".45" stop-color="#000" stop-opacity="0"/>
        <stop offset="1" stop-color="#000" stop-opacity=".85"/>
      </linearGradient>
      <linearGradient id="balloonFlight" x1="0" y1="0" x2="0" y2="1">
        <stop offset="0" stop-color="#4a2b1f"/>
        <stop offset=".55" stop-color="#6b4a30"/>
        <stop offset=".8" stop-color="#7a8a6a"/>
        <stop offset="1" stop-color="#6d7656"/>
      </linearGradient>
      <clipPath id="sunriseClip">
        <rect x="0" y="0" width="330" height="190"/>
        <circle cx="150" cy="180" r="162"/>
      </clipPath>
    </defs>
    <g role="img" aria-label="Photo of passengers filming a balloon at sunrise above the valley">
      <rect x="0" y="0" width="340" height="345" fill="url(#sunrise)" clip-path="url(#sunriseClip)"/>
      <rect x="0" y="0" width="340" height="345" fill="url(#shade)" clip-path="url(#sunriseClip)"/>
    </g>
    <rect x="330" y="0" width="20" height="190" fill="#f3f5f7" opacity=".6"/>
    <path d="M300 448 C 380 395 470 380 577 372 L577 448 Z" fill="var(--blue-bright)"/>
    <circle cx="470" cy="318" r="180" fill="none" stroke="var(--blue-bright)" stroke-width="9"/>
    <g role="img" aria-label="Photo of a brown and green hot air balloon above farmland">
      <circle cx="470" cy="318" r="172" fill="url(#balloonFlight)"/>
    </g>
    <circle cx="275" cy="288" r="76" fill="var(--white)"/>
    <circle cx="275" cy="288" r="70" fill="var(--blue-bright)" stroke="var(--ink-soft)" stroke-width="7"/>
    <rect x="190" y="396" width="366" height="26" rx="13" fill="var(--ink-soft)"/>
  </svg>

  <div class="abs offer" style="left:20px;top:158px">
    <div class="offer__title">WE<span class="script">offer</span></div>
    <ul class="offer__list">
      <li><svg class="tick" viewBox="0 0 10 10"><circle cx="5" cy="5" r="4.3" fill="none" stroke="#fff" stroke-width="1.2"/><path d="M3 5.2l1.4 1.4L7.2 3.8" fill="none" stroke="#fff" stroke-width="1.2"/></svg><span>Daily flights<br>over the Hunter Valley</span></li>
      <li><svg class="tick" viewBox="0 0 10 10"><circle cx="5" cy="5" r="4.3" fill="none" stroke="#fff" stroke-width="1.2"/><path d="M3 5.2l1.4 1.4L7.2 3.8" fill="none" stroke="#fff" stroke-width="1.2"/></svg><span>Champagne breakfast</span></li>
      <li><svg class="tick" viewBox="0 0 10 10"><circle cx="5" cy="5" r="4.3" fill="none" stroke="#fff" stroke-width="1.2"/><path d="M3 5.2l1.4 1.4L7.2 3.8" fill="none" stroke="#fff" stroke-width="1.2"/></svg><span>Digital flight photos</span></li>
      <li><svg class="tick" viewBox="0 0 10 10"><circle cx="5" cy="5" r="4.3" fill="none" stroke="#fff" stroke-width="1.2"/><path d="M3 5.2l1.4 1.4L7.2 3.8" fill="none" stroke="#fff" stroke-width="1.2"/></svg><span>Corporate flights</span></li>
      <li><svg class="tick" viewBox="0 0 10 10"><circle cx="5" cy="5" r="4.3" fill="none" stroke="#fff" stroke-width="1.2"/><path d="M3 5.2l1.4 1.4L7.2 3.8" fill="none" stroke="#fff" stroke-width="1.2"/></svg><span>Private flights</span></li>
      <li><svg class="tick" viewBox="0 0 10 10"><circle cx="5" cy="5" r="4.3" fill="none" stroke="#fff" stroke-width="1.2"/><path d="M3 5.2l1.4 1.4L7.2 3.8" fill="none" stroke="#fff" stroke-width="1.2"/></svg><span>Gift vouchers</span></li>
    </ul>
  </div>

  <div class="abs contact" style="left:215px;top:250px">
    <div class="contact__title">CONTACT<span class="script">us</span></div>
    <svg viewBox="0 0 10 10"><path d="M2.2 1h2l.8 2.2-1.2.9a6 6 0 0 0 2.1 2.1l.9-1.2L9 5.8v2A1.2 1.2 0 0 1 7.8 9 7.8 7.8 0 0 1 1 2.2 1.2 1.2 0 0 1 2.2 1z" fill="#fff"/></svg>
    <div class="contact__line">(1300 555 019)</div>
    <svg viewBox="0 0 10 10"><rect x="1" y="2.2" width="8" height="5.6" fill="none" stroke="#fff" stroke-width="1"/><path d="M1 2.4l4 3 4-3" fill="none" stroke="#fff" stroke-width="1"/></svg>
    <div class="contact__line">hello@skywardballooning.example</div>
  </div>

  <div class="abs" style="left:410px;top:22px">
    <div class="brand"><span class="brand__dot"></span>Skyward</div>
    <div class="brand__sub">Ballooning</div>
  </div>

  <div class="abs hotline" style="left:410px;top:68px">
    <div class="hotline__label">Booking Hot Line</div>
    <div class="hotline__num" style="margin-left:22px">1300</div>
    <div class="hotline__words">SKY RIDE</div>
  </div>

  <div class="abs hotline" style="left:28px;top:352px">
    <div class="hotline__label" style="margin-left:10px">Booking Hot Line</div>
    <div class="hotline__num" style="margin-left:26px">1300</div>
    <div class="hotline__words">SKY RIDE</div>
  </div>

  <div class="abs web" style="left:212px;top:405px"><i></i>www.skywardballooning.example</div>
  <div class="abs web" style="left:398px;top:405px"><i></i>www.skywardballooning.example</div>
</section>

<!-- Inside of the brochure -->
<section class="spread spread--inside">
  <svg class="shapes" viewBox="0 0 577 448">
    <defs>
      <linearGradient id="sky" x1="0" y1="0" x2="0" y2="1">
        <stop offset="0" stop-color="#3e74c4"/>
        <stop offset=".6" stop-color="#8db7e6"/>
        <stop offset="1" stop-color="#4d6a32"/>
      </linearGradient>
      <linearGradient id="darkBalloon" x1="0" y1="0" x2="0" y2="1">
        <stop offset="0" stop-color="#202a33"/>
        <stop offset=".7" stop-color="#2b3b45"/>
        <stop offset="1" stop-color="#6b6a4a"/>
      </linearGradient>
      <linearGradient id="fieldFade" x1="0" y1="0" x2="0" y2="1">
        <stop offset="0" stop-color="#ffffff"/>
        <stop offset="1" stop-color="#d7e3cf"/>
      </linearGradient>
      <clipPath id="leftPanel"><rect x="0" y="0" width="191" height="448"/></clipPath>
      <clipPath id="rightPanel"><rect x="384" y="0" width="193" height="448"/></clipPath>
    </defs>

    <rect x="0" y="120" width="191" height="328" fill="var(--blue-bright)"/>
    <path d="M0 132 C 60 108 130 108 191 124 L191 135 C 130 118 60 118 0 142 Z" fill="var(--ink-soft)"/>
    <path d="M0 0 H191 V124 C 130 108 60 108 0 132 Z" fill="var(--white)"/>
    <g clip-path="url(#leftPanel)">
      <circle cx="92" cy="348" r="100" fill="var(--white)"/>
      <g role="img" aria-label="Photo of a dark balloon with blue pattern seen from above">
        <circle cx="92" cy="348" r="94" fill="url(#darkBalloon)"/>
      </g>
    </g>

    <rect x="191" y="0" width="193" height="448" fill="var(--ink)"/>

    <rect x="384" y="0" width="193" height="448" fill="url(#fieldFade)"/>
    <g clip-path="url(#rightPanel)" role="img" aria-label="Photo of a balloon in a blue sky behind a vineyard tree">
      <rect x="384" y="0" width="193" height="150" fill="url(#sky)"/>
    </g>
    <path d="M384 118 C 440 160 520 160 577 130 L577 160 L384 160 Z" fill="url(#fieldFade)"/>
    <path d="M350 0 C 355 80 440 150 577 132" fill="none" stroke="var(--blue-bright)" stroke-width="9"/>
    <g role="img" aria-label="Faint photo of guests beside a balloon basket on the field">
      <rect x="384" y="330" width="193" height="118" fill="#cfdcc6" opacity=".5"/>
    </g>

    <rect x="191" y="392" width="366" height="27" rx="13.5" fill="var(--blue-bright)"/>
  </svg>

  <div class="abs hotline" style="left:28px;top:22px">
    <div class="hotline__label" style="margin-left:10px">Booking Hot Line</div>
    <div class="hotline__num" style="margin-left:26px">1300</div>
    <div class="hotline__words">SKY RIDE</div>
  </div>

  <div class="abs tagline" style="left:0;width:191px;top:150px">
    <span class="script">experience</span>
    <strong>the beautiful</strong>
    <strong>Hunter Valley</strong>
    <strong>in a hot</strong>
    <strong>air balloon.</strong>
  </div>

  <div class="abs feature" style="left:198px;width:178px;top:22px">
    <h3>Experienced</h3>
    <span class="script">pilot &amp; crew</span>
    <p>Skyward Ballooning pilots and crew are highly trained professionals which operate under the strict control of the National Air Safety Office. Skyward Ballooning deliver Australia, best hot air ballooning experience in a fun yet safe environment.</p>
  </div>

  <div class="abs feature" style="left:198px;width:178px;top:122px">
    <h3>Award Winning</h3>
    <span class="script">service</span>
    <p>Skyward Ballooning is an accredited tourism business and has been the winner of numerous State &amp; Regional Tourism awards. Skyward Ballooning strives to be the leader in the ballooning industry through all aspects of our business.</p>
  </div>

  <div class="abs feature" style="left:198px;width:178px;top:212px">
    <h3>Flight</h3>
    <span class="script">flexibility</span>
    <p>Skyward Ballooning offers a 100% flight fee refund if your flight is cancelled due to weather.</p>
  </div>

  <div class="abs" style="left:198px;width:178px;top:310px;display:flex;flex-direction:column;align-items:center">
    <div class="brand"><span class="brand__dot"></span>Skyward</div>
    <div class="brand__sub" style="color:var(--white)">Ballooning</div>
  </div>

  <div class="abs info" style="left:398px;width:166px;top:195px">
    <h3>Daily <span class="script">flights</span></h3>
    <p>Flights take place daily at sunrise in the Hunter Valley. Enjoy one hour of breathtaking views of Australia, oldest wine growing region and surrounds. A champagne breakfast concludes the morning at a local restaurant.</p>
  </div>

  <div class="abs info" style="left:398px;width:166px;top:262px">
    <h3>Digital Photo<br><span class="script">packages</span></h3>
    <p>Skyward Ballooning provides access to digital photography from all flights to capture those special moments for you to share with friends and family.</p>
  </div>

  <div class="abs web" style="left:212px;top:402px"><i></i>www.skywardballooning.example</div>
  <div class="abs web" style="left:398px;top:402px"><i></i>www.skywardballooning.example</div>
</section>

</body>
</html>
```